Meridian Lodging Partners

An Editable Business Card Template For MLP & MLH
Similar or Different Design

418 W. Harlan Brookside Pkwy.
Suite 2270
Irving, TX 75091

```html
<!DOCTYPE html>
<html lang="en">
<head>
<meta charset="UTF-8">
<title>Meridian Lodging Partners – Business Card</title>
<link href="https://fonts.googleapis.com/css2?family=Montserrat:wght@400;500;600&family=Libre+Baskerville:wght@700&display=swap" rel="stylesheet">
<style>
  :root {
    --backdrop: #2b2b2b;
    --card-dark: #0c0c0c;
    --card-light: #ffffff;
    --brand-red: #b5282b;
    --text-light: #f2f2f2;
    --text-dark: #2a2a2a;
    --muted: #555555;
  }
  * { margin: 0; padding: 0; box-sizing: border-box; }
  html, body { width: 1200px; height: 1186px; overflow: hidden; }
  body {
    background: var(--backdrop);
    font-family: "Montserrat", sans-serif;
    position: relative;
  }
  .card {
    position: absolute;
    left: 150px;
    width: 900px;
    height: 514px;
    border-radius: 34px;
    overflow: hidden;
  }
  .card--back { top: 60px; background: var(--card-dark); color: var(--text-light); }
  .card--front { top: 612px; background: var(--card-light); color: var(--text-dark); }

  .company-name {
    position: absolute;
    left: 70px;
    top: 50%;
    transform: translateY(-50%);
    width: 300px;
    font-weight: 600;
    font-size: 28px;
    line-height: 1.3;
  }
  .card--back .company-name { color: var(--text-light); }
  .card--front .company-name { color: var(--text-dark); }

  .benefits {
    position: absolute;
    left: 440px;
    top: 118px;
    list-style: none;
    font-size: 20px;
    font-weight: 500;
    line-height: 1.3;
  }
  .benefits li {
    position: relative;
    padding-left: 22px;
    margin-bottom: 14px;
  }
  .benefits li::before {
    content: "";
    position: absolute;
    left: 0; top: 9px;
    width: 8px; height: 8px;
    border-radius: 50%;
    background: var(--brand-red);
  }

  .contact {
    position: absolute;
    left: 500px;
    top: 120px;
  }
  .contact__name {
    font-family: "Libre Baskerville", serif;
    font-weight: 700;
    font-size: 34px;
    color: var(--brand-red);
  }
  .contact__title {
    font-size: 19px;
    color: var(--muted);
    margin: 4px 0 26px;
  }
  .contact__list { list-style: none; font-size: 19px; }
  .contact__list li {
    display: flex;
    align-items: center;
    gap: 12px;
    margin-bottom: 8px;
  }
  .contact__list svg { width: 16px; height: 16px; fill: var(--brand-red); flex: none; }
  .contact__address {
    font-style: normal;
    font-size: 19px;
    line-height: 1.35;
    margin-top: 26px;
  }
</style>
</head>
<body>
  <section class="card card--back">
    <p class="company-name">Meridian Lodging Partners</p>
    <ul class="benefits">
      <li>Proven Track Record Of Performance</li>
      <li>Live Customer Support 24/7/365</li>
      <li>Experienced Lodging Provider<br>To Various Corporate Industries</li>
      <li>Consolidated Billing/Administration</li>
      <li>Full-Service Lodging Including<br>Multiple Long-Term Options</li>
      <li>No Additional Fees</li>
    </ul>
  </section>

  <section class="card card--front">
    <p class="company-name">Meridian Lodging Partners</p>
    <div class="contact">
      <h1 class="contact__name">Dana Whitfield</h1>
      <p class="contact__title">Sales Manager</p>
      <ul class="contact__list">
        <li>
          <svg viewBox="0 0 16 16" aria-hidden="true"><path d="M3 1h3l1.5 3.5-2 1.3a9 9 0 0 0 4.7 4.7l1.3-2L15 10v3a2 2 0 0 1-2 2A12 12 0 0 1 1 3a2 2 0 0 1 2-2z"/></svg>
          214.555.0148
        </li>
        <li>
          <svg viewBox="0 0 16 16" aria-hidden="true"><path d="M1 3h14v10H1z M1 3l7 6 7-6" stroke="#fff" stroke-width="1.2"/></svg>
          dwhitfield@meridianlp.com
        </li>
        <li>
          <svg viewBox="0 0 16 16" aria-hidden="true"><circle cx="8" cy="8" r="7"/><path d="M1 8h14M8 1c3 3 3 11 0 14M8 1c-3 3-3 11 0 14" stroke="#fff" stroke-width="1" fill="none"/></svg>
          www.meridianlp.com
        </li>
      </ul>
      <address class="contact__address">
        418 W. Harlan Brookside Pkwy.<br>
        Suite 2270, Irving, TX 75091
      </address>
    </div>
  </section>
</body>
</html>
```